Managed IT services business card design

We haven't needed a business card since the founding of the business in 2005. All our clients have been coming through word of mouth. And lately more and more existing clients are requesting for our business cards to pass on to their contacts in recommending us.
So we needing a business card design. We use various innovative solutions and methodologies to provide IT services to small businesses in managing their IT systems. Our role is the same as an in-house, full-time IT Manager for our clients, but outsourced. So we take care of all our clients' IT needs, just as an IT Manager would be expected to perform.
We have a holding website, which we're happy to leave for now. If we can use the same logo would be great - www.lomvex.com.au
Preferred colours are shades of are white, grey and black.
We pride our business with the following traits: proactive, good service, prompt response, trustworthy.
Target Market(s)
Small businesses of any industry
Industry/Entity Type
Business

```html
<!DOCTYPE html>
<html lang="en">
<head>
<meta charset="utf-8">
<title>Lomvex business card</title>
<link rel="stylesheet" href="https://fonts.googleapis.com/css2?family=Open+Sans:wght@400&display=swap">
<style>
  :root {
    --backdrop: #d6d6d6;
    --card: #ffffff;
    --ink: #111111;
    --icon: #5a5a5a;
  }
  * { margin: 0; padding: 0; box-sizing: border-box; }
  html, body {
    width: 1200px;
    height: 900px;
    overflow: hidden;
    background: var(--backdrop);
    font-family: "Open Sans", sans-serif;
    color: var(--ink);
  }
  .card {
    position: absolute;
    left: 150px;
    top: 170px;
    width: 900px;
    height: 560px;
    background: var(--card);
    border-radius: 42px;
    box-shadow: 0 18px 40px rgba(0, 0, 0, 0.18);
    overflow: hidden;
  }
  .brand {
    position: absolute;
    left: 0;
    right: 0;
    top: 128px;
    display: flex;
    justify-content: center;
    align-items: center;
    gap: 18px;
  }
  .brand-mark {
    width: 20px;
    height: 20px;
    background: var(--ink);
  }
  .brand-name {
    font-weight: 400;
    font-size: 54px;
    line-height: 1;
  }
  .rule {
    position: absolute;
    left: 0;
    right: 0;
    top: 292px;
    height: 5px;
    background: var(--ink);
  }
  .divider {
    position: absolute;
    left: 540px;
    top: 334px;
    width: 2px;
    height: 180px;
    background: var(--ink);
  }
  .person {
    position: absolute;
    right: 390px;
    top: 378px;
    text-align: right;
  }
  .person-name {
    font-size: 27px;
    line-height: 1.2;
  }
  .person-role {
    font-size: 18px;
    line-height: 1.3;
  }
  .contacts {
    position: absolute;
    left: 565px;
    top: 334px;
    list-style: none;
  }
  .contact {
    display: flex;
    align-items: flex-start;
    font-size: 21px;
    line-height: 29px;
  }
  .contact svg {
    width: 22px;
    height: 22px;
    margin-top: 4px;
    margin-right: 10px;
    flex: none;
    fill: var(--icon);
  }
</style>
</head>
<body>
  <div class="card">
    <div class="brand">
      <span class="brand-mark"></span>
      <span class="brand-name">Lomvex</span>
    </div>
    <div class="rule"></div>

    <div class="person">
      <div class="person-name">Firstname Lastname</div>
      <div class="person-role">manager</div>
    </div>

    <div class="divider"></div>

    <ul class="contacts">
      <li class="contact">
        <svg viewBox="0 0 24 24" aria-hidden="true"><path d="M6.6 10.8c1.4 2.8 3.8 5.1 6.6 6.6l2.2-2.2c.3-.3.7-.4 1-.2 1.1.4 2.3.6 3.6.6.6 0 1 .4 1 1V20c0 .6-.4 1-1 1C10.6 21 3 13.4 3 4c0-.6.4-1 1-1h3.5c.6 0 1 .4 1 1 0 1.3.2 2.5.6 3.6.1.3 0 .7-.2 1L6.6 10.8z"/></svg>
        <span>02 5550 4133</span>
      </li>
      <li class="contact">
        <svg viewBox="0 0 24 24" aria-hidden="true"><path d="M7 2h8l3 3v4H7V2zm-3 8h16a2 2 0 0 1 2 2v6h-4v4H6v-4H2v-6a2 2 0 0 1 2-2zm4 7v3h8v-3H8z"/></svg>
        <span>02 5550 2990</span>
      </li>
      <li class="contact">
        <svg viewBox="0 0 24 24" aria-hidden="true"><path d="M2 5h20v14H2V5zm2 2v.4l8 5.2 8-5.2V7H4zm0 2.8V17h16V9.8l-8 5.2-8-5.2z"/></svg>
        <span>info@www.lomvex.com.au</span>
      </li>
      <li class="contact">
        <svg viewBox="0 0 24 24" aria-hidden="true"><path d="M12 2a10 10 0 1 0 0 20 10 10 0 0 0 0-20zm6.9 6h-3a15 15 0 0 0-1.3-3.9A8 8 0 0 1 18.9 8zM12 4c.8 1.2 1.5 2.5 1.9 4h-3.8c.4-1.5 1.1-2.8 1.9-4zM4.3 14a8 8 0 0 1 0-4h3.4a16 16 0 0 0 0 4H4.3zm.8 2h3a15 15 0 0 0 1.3 3.9A8 8 0 0 1 5.1 16zm3-8h-3a8 8 0 0 1 4.3-3.9C8.8 5.3 8.4 6.6 8.1 8zM12 20c-.8-1.2-1.5-2.5-1.9-4h3.8c-.4 1.5-1.1 2.8-1.9 4zm2.3-6H9.7a14 14 0 0 1 0-4h4.6a14 14 0 0 1 0 4zm.3 5.9c.6-1.200 1-2.5 1.3-3.9h3a8 8 0 0 1-4.3 3.9zm1.7-5.9a16 16 0 0 0 0-4h3.4a8 8 0 0 1 0 4h-3.4z"/></svg>
        <span>www.lomvex.com.au</span>
      </li>
      <li class="contact">
        <svg viewBox="0 0 24 24" aria-hidden="true"><path d="M12 3 1 12h3v9h6v-6h4v6h6v-9h3L12 3z"/></svg>
        <span>18 Kestrel Road Marden<br>NSW 2570, London</span>
      </li>
    </ul>
  </div>
</body>
</html>
```